Tobias Wrenfield - Cinematographer

NEED:
I'm looking for a sleek, professional, modern business card that will give give the recipient the impression that they can trust their production will go smoothly by hiring me. I will bring creativity and knowledge to their shoot, so that we can create powerful images.
I am looking for a card with a strong style and design ethos that could be expanded to a website and a full visual/graphic/design entity for me.
ABOUT ME:
I am a mid-twenties cinematographer, I work on music video, narrative short, commercial, and corporate projects. I blend the science and artistry of cameras and filmmaking to tell a story. I'm an artist, a technician, and a manager.
DESIGN:
I like sleek, simple design. Black, dark grays, white, dark navy, steel blues, I love cyan, but also cyan and red. I am not a fan of earthy tones. I generally prefer modern, san-serif fonts over serifs. My old logo was based on an aperture, a multi-blade device at the back of a lens that controls how much light passes through, but I made it with so many colors, that it doesn't necessarily lend itself to a specific color-scheme or design ethos. I liked that the aperture design provided a sense of the technical requirements of my job. I'm a fan of matte business cards, but am open to plenty of specialty print processes to make an outstanding card.
ATTACHED FILES:
My Old Rainbox Aperture Logo, plus a few designs I've tried playing around with, but am not tied to. I AM OPEN TO NEW DESIGNS, DO NOT FEEL TIED TO THIS.
**I've pulled my old logo down from the attached files, and instead attached other business cards I like, so as not to mislead you where I would like to go.
INFO:
Name: Tobias Wrenfield
Job: Cinematographer
Email: tkwrenfield@quillbox.example
Phone: 503.618.2907
Website: tobiaswrenfield.example
Updates
I'm adding some images of other cards that I like, and removing my old logo, since I'm looking for something new, and don't want that old logo to push anyone a certain direction.

```html
<!DOCTYPE html>
<html lang="en">
<head>
<meta charset="utf-8">
<title>Tobias Wrenfield – Cinematographer</title>
<link rel="stylesheet" href="https://fonts.googleapis.com/css2?family=Inter:wght@100;200;400&display=swap">
<style>
  :root {
    --navy: #0e2644;
    --name-grey: #9a9a9c;
    --light: #e4e4e4;
    --bar: #d4d4d4;
    --ring: #a19e9f;
    --aperture-grey: #5b5b5d;
  }
  html, body {
    margin: 0;
    padding: 0;
    overflow: hidden;
    background: var(--navy);
  }
  .card {
    position: relative;
    width: 1200px;
    height: 686px;
    background: var(--navy);
    overflow: hidden;
    font-family: "Inter", "Helvetica Neue", Arial, sans-serif;
  }
  .card-art {
    position: absolute;
    inset: 0;
    display: block;
  }
  .name-first { fill: var(--name-grey); font-weight: 400; }
  .name-last { fill: var(--light); font-weight: 100; }
  .name { font-size: 78px; }
  .title-rule { fill: var(--bar); }
  .job-title {
    fill: var(--light);
    font-size: 31px;
    font-weight: 200;
  }
  .aperture-ring { fill: none; stroke: var(--ring); stroke-width: 14; }
  .aperture-fill { fill: var(--aperture-grey); }
  .contact-list {
    position: absolute;
    left: 24px;
    top: 396px;
    margin: 0;
    padding: 0;
    list-style: none;
  }
  .contact-item {
    display: flex;
    align-items: center;
    height: 34px;
    margin-bottom: 33px;
    color: var(--light);
    font-size: 32px;
    font-weight: 400;
    letter-spacing: 0.2px;
  }
  .contact-icon {
    width: 32px;
    height: 32px;
    margin-right: 26px;
    flex: none;
    fill: none;
    stroke: var(--light);
    stroke-width: 2;
  }
  .contact-icon .solid { fill: var(--light); stroke: none; }
</style>
</head>
<body>
  <div class="card">
    <svg class="card-art" width="1200" height="686" viewBox="0 0 1200 686" aria-hidden="false">
      <text class="name" x="24" y="109" textLength="650" lengthAdjust="spacingAndGlyphs"><tspan class="name-first">TOBIAS</tspan><tspan class="name-last">WRENFIELD</tspan></text>
      <path class="title-rule" d="M0 131 H668 a7 7 0 0 1 0 14 H0 Z"/>
      <text class="job-title" x="25" y="194" textLength="648" lengthAdjust="spacing">CINEMATOGRAPHER</text>

      <circle class="aperture-ring" cx="966" cy="537" r="385"/>
      <circle class="aperture-fill" cx="966" cy="537" r="368" role="img" aria-label="Lens aperture illustration: grey iris blades on navy"/>
    </svg>

    <ul class="contact-list">
      <li class="contact-item">
        <svg class="contact-icon" viewBox="0 0 32 32" aria-hidden="true">
          <rect x="9" y="5" width="14" height="24" rx="2"/>
          <rect class="solid" x="12" y="9" width="8" height="6"/>
          <rect class="solid" x="12" y="18" width="2" height="2"/><rect class="solid" x="15" y="18" width="2" height="2"/><rect class="solid" x="18" y="18" width="2" height="2"/>
          <rect class="solid" x="12" y="22" width="2" height="2"/><rect class="solid" x="15" y="22" width="2" height="2"/><rect class="solid" x="18" y="22" width="2" height="2"/>
        </svg>
        <span class="contact-text">503.618.2907</span>
      </li>
      <li class="contact-item">
        <svg class="contact-icon" viewBox="0 0 32 32" aria-hidden="true">
          <path d="M3 13 L16 4 L29 13 V28 H3 Z"/>
          <path d="M3 13 L16 21 L29 13"/>
          <path d="M3 28 L13 19 M29 28 L19 19"/>
        </svg>
        <span class="contact-text">tkwrenfield@quillbox.example</span>
      </li>
      <li class="contact-item">
        <svg class="contact-icon" viewBox="0 0 32 32" aria-hidden="true">
          <circle cx="16" cy="16" r="13"/>
          <ellipse cx="16" cy="16" rx="6" ry="13"/>
          <path d="M16 3 V29 M3 16 H29 M5 9 H27 M5 23 H27"/>
        </svg>
        <span class="contact-text">tobiaswrenfield.example</span>
      </li>
    </ul>
  </div>
</body>
</html>
```